Luxury new home community needs a contemporary and high end looking brochure

We need a brochure to introduce a luxury new home community. The brochure needs to have a modern and high end look and feel while still keeping nature a predominant theme.
The "purpose.doc" describes the text and must have images for each page. The "BrandGuidelines.pdf" includes the color palette. The "11x17 halffold-inside.jpg and 11x17halffold-outside.jpg" files include the print guidelines that must be met.
The additional images downloaded can be used at your discretion-be creative! I prefer Photoshop files please. Additional information about our new home community can be found at www.HollowbrookMeadowsKS.example

Target Market(s)

High Net Worth Individuals
Real Estate Agents

Industry/Entity Type

Real Estate

Requirements
Must have
• Please see Purpose.doc for required text and images
• Please see BrandGuidelines.pdf for color palette and fonts

```html
<!DOCTYPE html>
<html lang="en">
<head>
<meta charset="utf-8">
<title>Hollowbrook Meadows Brochure Covers</title>
<link rel="stylesheet" href="https://fonts.googleapis.com/css2?family=Montserrat:wght@400;600;700&family=Roboto+Condensed:wght@700&family=Roboto:wght@400&display=swap">
<style>
  :root {
    --bg: #cfe0dc;
    --ink: #111111;
    --white: #ffffff;
    --rock-dark: #2f2e2b;
    --rock-mid: #5a5650;
    --rock-light: #7d776e;
    --sky: #5d8fd0;
    --cloud: #dfe6ee;
    --house: #8a6a4c;
    --lawn: #5f7d2c;
    --lawn-dark: #4a6422;
    --map-bg: #f6f6f4;
    --map-road: #8b7a55;
  }
  * { box-sizing: border-box; margin: 0; padding: 0; }
  html, body { width: 1200px; height: 824px; overflow: hidden; }
  body {
    background: var(--bg);
    display: flex; align-items: center; justify-content: center;
    font-family: "Montserrat", sans-serif;
  }
  .spread { display: flex; width: 1160px; height: 750px; box-shadow: 0 10px 30px rgba(0,0,0,.25); }
  .page { position: relative; width: 580px; height: 750px; overflow: hidden; }

  /* Back cover */
  .back-cover { color: var(--white); }
  .back-cover .photo-rocks {
    position: absolute; inset: 0;
    background:
      radial-gradient(ellipse at 30% 20%, rgba(120,112,100,.6), transparent 60%),
      radial-gradient(ellipse at 70% 70%, rgba(90,85,78,.7), transparent 60%),
      linear-gradient(160deg, var(--rock-dark), var(--rock-mid) 45%, var(--rock-light) 70%, var(--rock-dark));
  }
  .back-cover .content { position: absolute; left: 62px; right: 50px; top: 110px; }
  .wordmark { text-align: center; }
  .wordmark .mark-square { display: inline-block; width: 56px; height: 56px; background: var(--white); margin-bottom: 14px; }
  .wordmark .name { font-weight: 600; font-size: 44px; letter-spacing: 2px; line-height: 1; white-space: nowrap; }
  .wordmark .sub { font-weight: 600; font-size: 13px; letter-spacing: 12px; margin-top: 8px; }
  .location-lead { font-weight: 700; font-size: 15px; line-height: 1.25; margin-top: 34px; }
  .location-body { font-size: 12.5px; line-height: 1.35; margin-top: 6px; }
  .contact { font-weight: 700; font-size: 15px; line-height: 1.6; margin-top: 36px; }
  .developer {
    position: absolute; right: 40px; top: 552px;
    display: flex; align-items: center; gap: 8px;
    font-size: 12px; letter-spacing: 4px; font-weight: 400; line-height: 1.3;
  }
  .developer .dot { width: 24px; height: 24px; border-radius: 50%; background: var(--white); flex: none; }
  .map { position: absolute; background: var(--map-bg); border: 3px solid var(--map-road); }
  .map-region { left: 62px; top: 620px; width: 290px; height: 112px; }
  .map-local { left: 372px; top: 594px; width: 170px; height: 100px; }

  /* Front cover */
  .front-cover .photo-home {
    position: absolute; inset: 0;
    background:
      radial-gradient(ellipse at 50% 48%, var(--house) 0, rgba(138,106,76,.8) 22%, transparent 45%),
      linear-gradient(180deg, var(--sky) 0, var(--cloud) 16%, var(--sky) 28%, #9fb2c4 38%, var(--house) 47%, var(--lawn) 58%, var(--lawn-dark) 100%);
    filter: blur(2px);
  }
  .front-cover .frame {
    position: absolute; left: 50px; right: 50px; top: 140px;
    border: 2px solid var(--ink);
    color: var(--ink); text-align: center;
    padding: 36px 40px 34px;
  }
  .intro { font-family: "Roboto Condensed", sans-serif; font-weight: 700; font-size: 23px; line-height: 1.2; }
  .front-cover .wordmark { margin-top: 24px; }
  .front-cover .wordmark .mark-square { background: var(--ink); width: 60px; height: 60px; }
  .front-cover .wordmark .name { font-size: 42px; }
  .tagline { font-family: "Roboto", sans-serif; font-size: 20px; line-height: 1.7; margin-top: 30px; }
</style>
</head>
<body>
  <main class="spread">
    <section class="page back-cover">
      <div class="photo-rocks" role="img" aria-label="Photograph of a rocky creek bed with stones and shallow water"></div>
      <div class="content">
        <div class="wordmark">
          <span class="mark-square"></span>
          <div class="name">HOLLOWBROOK</div>
          <div class="sub">· MEADOWS ·</div>
        </div>
        <p class="location-lead">Conveniently located ½ mile west of K-7 on 127th Street, Westmoor, KS</p>
        <p class="location-body">The peaceful enclave of Hollowbrook Meadows is nestled in the heart of the K-7 growth corridor, giving homeowners convenient access to shops, services, dining, entertainment and recreation throughout Johnson County and the larger Kansas City metro area.</p>
        <p class="contact">HollowbrookMeadowsKS.example<br>(913) 555-0142</p>
      </div>
      <div class="developer"><span class="dot"></span><span>CRESTLINE<br>DEVELOPMENT</span></div>
      <div class="map map-region" role="img" aria-label="Regional map showing highways and landmarks around the community"></div>
      <div class="map map-local" role="img" aria-label="Local street map showing the community entrance near 127th Street"></div>
    </section>

    <section class="page front-cover">
      <div class="photo-home" role="img" aria-label="Softly blurred photograph of a luxury stone home under a blue sky with a green lawn"></div>
      <div class="frame">
        <p class="intro">Introducing Westmoor's newest<br>Luxury New Home Community</p>
        <div class="wordmark">
          <span class="mark-square"></span>
          <div class="name">HOLLOWBROOK</div>
          <div class="sub">· MEADOWS ·</div>
        </div>
        <p class="tagline">36 Heavily Wooded Estate Sized Lots<br>Custom Homes from $1 Million</p>
      </div>
    </section>
  </main>
</body>
</html>
```